Used Car Business Card Design

Maple Ridge Auto Sales is a woman owned women friendly car lot.  We focus on providing Professionalism, Integrity and Respect beginning with the initial introduction.  We place the highest importance on customer service after the sale and our rating with the TVB of Arkansas shows it.  We're starting out 7th year, recently relocated. Satisfied Clients bring their family members, friends and co-workers to buy their cars, SUV's and trucks from MRAS.
You buy here / you pay here, Lending program opportunities too, Great Cash Prices
Finance with Flexibility we look at each individual uniquely and not a credit score
I think of my kids when getting our vehicles ready and your safety when you drive away in a MRAS car. . .  Drive away with Peace of Mind...
Maroon, Black and Silver colors.

Updates
I sent a response to the designers - have  not heard from them, will I receive my funds back?

Thank you all,  a lot of great designs - Making my decision on Nov 4th

So much talent. . .
So very challenging. . .
Thank you for your participation.
Sincerely,
Maple Ridge Auto Sales
Lorna Pickett

Industry/Entity Type
Safety
Contact Information for Business Card
Maple Ridge Auto Sales
"A Sound Car for a Fair Price"
4153 Garvey Rd. Cedar Falls, TN 38301
Lorna Pickett
731.389.7312

```html
<!DOCTYPE html>
<html lang="en">
<head>
<meta charset="utf-8">
<title>Maple Ridge Auto Sales – Business Card</title>
<link rel="stylesheet" href="https://fonts.googleapis.com/css2?family=Cinzel+Decorative:wght@700&family=Alegreya:ital,wght@1,400;1,500;1,700&display=swap">
<style>
  :root {
    --maroon: #8a1a20;
    --maroon-dark: #6e1318;
    --maroon-light: #9a2328;
    --silver: #e4e4e4;
    --silver-soft: #d6d6d6;
    --ink: #111111;
    --paper: #ffffff;
    --backdrop: #ece9e4;
  }
  * { margin: 0; padding: 0; box-sizing: border-box; }
  html, body {
    width: 1200px; height: 800px; overflow: hidden;
    background: var(--backdrop);
  }
  .canvas { position: relative; width: 1200px; height: 800px; }

  .card {
    position: absolute; left: 233px; width: 555px; height: 323px;
    overflow: hidden;
    box-shadow: 0 3px 10px rgba(0,0,0,0.18);
  }

  /* Front */
  .card--front {
    top: 98px;
    background: radial-gradient(ellipse at 40% 40%, var(--maroon-light), var(--maroon) 55%, var(--maroon-dark));
    text-align: center;
  }
  .card--front .company {
    position: absolute; left: 0; right: 0; top: 132px;
    font-family: "Cinzel Decorative", serif; font-weight: 700;
    font-size: 30px; color: var(--silver); letter-spacing: 0.5px;
  }
  .card--front .tagline {
    position: absolute; left: 0; right: 0; top: 174px;
    font-family: "Alegreya", serif; font-style: italic;
    font-size: 24px; color: var(--silver-soft);
  }

  /* Back */
  .card--back { top: 429px; background: var(--paper); }
  .card--back .wave { position: absolute; left: 0; top: 0; width: 555px; height: 323px; }
  .card--back .company {
    position: absolute; left: 34px; top: 42px;
    font-family: "Cinzel Decorative", serif; font-weight: 700;
    font-size: 23px; color: var(--maroon);
  }
  .card--back .motto {
    position: absolute; left: 125px; top: 75px;
    font-family: "Alegreya", serif; font-style: italic; font-weight: 500;
    font-size: 18px; color: var(--ink);
  }
  .card--back .person {
    position: absolute; right: 33px; top: 139px;
    font-family: "Alegreya", serif; font-style: italic;
    font-size: 23px; color: var(--maroon); letter-spacing: 0.5px;
    text-transform: uppercase;
  }
  .contact {
    position: absolute; right: 33px; top: 192px;
    font-family: "Alegreya", serif; font-style: italic;
    font-size: 14.5px; color: var(--ink); text-align: right; line-height: 22px;
    list-style: none;
  }
  .contact .label { color: var(--maroon); }
</style>
</head>
<body>
<main class="canvas">
  <section class="card card--front">
    <h1 class="company">Maple Ridge Auto Sales</h1>
    <p class="tagline">A Sound Car for a Fair Price</p>
  </section>

  <section class="card card--back">
    <svg class="wave" viewBox="0 0 555 323" aria-hidden="true">
      <path d="M0,206 C90,196 170,225 250,258 C330,290 440,290 555,270 L555,323 L0,323 Z" fill="var(--maroon)"/>
      <path d="M0,188 C90,180 170,215 250,252 C330,286 440,286 555,264 L555,268 C440,290 330,292 250,262 C170,228 90,200 0,200 Z" fill="var(--ink)"/>
    </svg>
    <h2 class="company">Maple Ridge Auto Sales</h2>
    <p class="motto">Buy Here, Pay Here.</p>
    <p class="person">Lorna Pickett</p>
    <ul class="contact">
      <li><span class="label">P:</span> 731.389.7312</li>
      <li><span class="label">A:</span> 4153 Garvey Rd. Cedar Falls,</li>
      <li>TN 38301</li>
    </ul>
  </section>
</main>
</body>
</html>
```